Upsell Vertical Banner Ad Design For B2B Marketing Agency Vertical 768px × 1180px IS THE SIZE

I need a banner made for my website www.brightlanepromotionhub.biz This banner will be an upsell advertisement for after someone signs up for my monthly program. When they login to their account for the 1st time I will give them the chance to upgrade their account to our annual program with just one click.

this is a page that upsells it currently to give you an idea how we market ourselves:
https://tlpx.pagevault-example.com/page/tlp-annual-upsell

Use this content:

Are You Ready To Commit To Taking Your Business To The Next Level?

Because We're In This For The Long-Haul and Dedicated To Your Success...

Save $300 By Upgrading To An Annual Membership And Pay Only $74/mth

((BUTTON))Yes, Upgrade My Plan Right Now!

*Must prepay the full year at only $898/yr!

Target Market(s)

business owners

Industry/Entity Type

Marketing

Requirements
Must have
• 768px × 1180px IS THE SIZE vertical

Use this content:

Nice to have
• Use this content:

Should not have
• Use this content:

```html
<!DOCTYPE html>
<html lang="en">
<head>
<meta charset="utf-8">
<title>Annual Upgrade Banner – Bright Lane Promotion Hub</title>
<link rel="stylesheet" href="https://fonts.googleapis.com/css2?family=Rajdhani:wght@500;600;700&display=swap">
<style>
  :root {
    --blue-deep: #0a4a93;
    --blue-mid: #0d5cab;
    --blue-bubble: #0a87d8;
    --green-btn: #4cad4e;
    --green-leaf-1: #3f9a3a;
    --green-leaf-2: #7cc15c;
    --office-light: #e9edf0;
    --office-mid: #b9c3cb;
    --office-warm: #c89a6c;
    --white: #ffffff;
  }
  html, body {
    margin: 0;
    width: 781px;
    height: 1200px;
    overflow: hidden;
    background: var(--blue-deep);
  }
  .banner {
    position: relative;
    width: 768px;
    height: 1180px;
    transform: scale(1.01693);
    transform-origin: 0 0;
    overflow: hidden;
    font-family: "Rajdhani", sans-serif;
    color: var(--white);
    text-align: center;
  }
  .banner-art {
    position: absolute;
    inset: 0;
    width: 768px;
    height: 1180px;
  }
  .headline {
    position: absolute;
    top: 48px;
    left: 0;
    width: 768px;
    margin: 0;
    font-weight: 700;
    font-size: 50px;
    line-height: 65px;
    letter-spacing: 1.5px;
    text-transform: uppercase;
  }
  .subline {
    position: absolute;
    top: 285px;
    left: 0;
    width: 768px;
    margin: 0;
    font-weight: 500;
    font-size: 29px;
    line-height: 38px;
  }
  .offer {
    position: absolute;
    top: 402px;
    left: 0;
    width: 768px;
    margin: 0;
    font-weight: 700;
    font-size: 29px;
    line-height: 40px;
  }
  .cta-button {
    position: absolute;
    top: 523px;
    left: 190px;
    width: 388px;
    height: 68px;
    border-radius: 34px;
    background: var(--green-btn);
    color: var(--white);
    font-family: "Rajdhani", sans-serif;
    font-weight: 700;
    font-size: 20px;
    line-height: 68px;
    text-transform: uppercase;
    text-decoration: none;
  }
  .prepay-note {
    position: absolute;
    top: 686px;
    left: 420px;
    width: 240px;
    margin: 0;
    font-weight: 700;
    font-size: 25px;
    line-height: 34px;
  }
  .brand-name {
    position: absolute;
    top: 1113px;
    left: 400px;
    width: 350px;
    margin: 0;
    font-weight: 600;
    font-size: 22px;
    line-height: 28px;
    letter-spacing: 1.5px;
    text-transform: uppercase;
    text-align: right;
  }
</style>
</head>
<body>
  <main class="banner">
    <svg class="banner-art" viewBox="0 0 768 1180" aria-hidden="false">
      <defs>
        <linearGradient id="sky" x1="0" y1="0" x2="0" y2="1">
          <stop offset="0" stop-color="#0b4b95"/>
          <stop offset="1" stop-color="#0e5fae"/>
        </linearGradient>
        <linearGradient id="office" x1="0" y1="0" x2="1" y2="1">
          <stop offset="0" stop-color="var(--office-light)"/>
          <stop offset="0.45" stop-color="var(--office-mid)"/>
          <stop offset="0.7" stop-color="var(--office-warm)"/>
          <stop offset="1" stop-color="#d9dde0"/>
        </linearGradient>
        <linearGradient id="leaves" x1="0" y1="0" x2="1" y2="1">
          <stop offset="0" stop-color="var(--green-leaf-2)"/>
          <stop offset="1" stop-color="var(--green-leaf-1)"/>
        </linearGradient>
      </defs>
      <rect class="background-field" width="768" height="1180" fill="url(#sky)"/>
      <polygon class="office-photo" role="img"
               aria-label="Photo of two colleagues working together at a desk in a bright modern office"
               points="0,485 768,1000 768,1180 0,1180" fill="url(#office)"/>
      <circle class="note-bubble" cx="548" cy="850" r="205" fill="var(--blue-bubble)"/>
      <polygon class="foliage-corner" role="img"
               aria-label="Soft-focus green foliage"
               points="768,675 768,1180 245,1180" fill="url(#leaves)"/>
    </svg>

    <h1 class="headline">Are You Ready To Commit<br>To Taking Your Business<br>To The Next Level?</h1>
    <p class="subline">Because We're In This For The Long-Haul<br>and Dedicated To Your Success...</p>
    <p class="offer">Save $300 By Upgrading To An Annual<br>Membership And Pay Only $74/mth</p>
    <a class="cta-button" href="https://tlpx.pagevault-example.com/page/tlp-annual-upsell">Yes, Upgrade My Plan Right Now!</a>
    <p class="prepay-note">*Must prepay<br>the full year at<br>only $898/yr!</p>
    <p class="brand-name">Bright Lane Promotion Hub</p>
  </main>
</body>
</html>
```